Accounting business needs a fridge magnet design

I need a business card size design to be used as a fridge magnet.
It will need to be vertical not horizontal and it will have my logo and the services I provide listed below it.
It needs to be pleasing to the eye and catch peoples attention.
I have uploaded my current business card as a reference.
It can look totally different though, i am open to new ideas.

It will need to say:

Specialising in:
*Small Business Taxation
*Company & Trust Returns
*Financial Statements
*Partnership Taxation
*BAS preparation/lodgement
*Capital Gains Tax
*Business Start Ups
*Business Structuring
*Tax Planning

```html
<!DOCTYPE html>
<html lang="en">
<head>
<meta charset="utf-8">
<title>Northline Tax – Fridge Magnet</title>
<link rel="stylesheet" href="https://fonts.googleapis.com/css2?family=Lato:wght@700;900&family=Montserrat:wght@400&display=swap">
<style>
  :root {
    --page: #ffffff;
    --linen: #8c8c8c;
    --linen-dark: #777777;
    --silver-light: #ffffff;
    --silver-mid: #e6e6e6;
    --silver-dark: #b9b9b9;
    --ink: #1f1f1f;
    --ribbon-text: #ffffff;
    --navy: #003a74;
    --navy-fold: #00264d;
    --ocean: #035f92;
    --ocean-fold: #024165;
    --teal: #0389ac;
    --teal-fold: #025e77;
    --aqua: #06bcd6;
    --aqua-fold: #048196;
    --sky: #03c3ef;
    --sky-fold: #0287a6;
    --lagoon: #03c0d8;
    --lagoon-fold: #028497;
  }
  * { box-sizing: border-box; margin: 0; padding: 0; }
  html, body { width: 1200px; height: 1200px; overflow: hidden; background: var(--page); }
  .canvas { position: relative; width: 1200px; height: 1200px; }

  .magnet {
    position: absolute; left: 360px; top: 181px;
    width: 478px; height: 838px;
    border-radius: 16px; overflow: hidden;
    background: linear-gradient(90deg, var(--linen-dark), var(--linen) 20%, var(--linen) 80%, var(--linen-dark));
  }
  .silver-panel {
    position: absolute; left: 44px; top: 0; width: 396px; height: 100%;
    background: radial-gradient(ellipse at 50% 20%, var(--silver-light) 0%, var(--silver-mid) 45%, var(--silver-dark) 100%);
  }
  .brand-mark {
    position: absolute; left: 193px; top: 16px; width: 92px; height: 92px;
    border: 2px solid var(--ink); border-radius: 50%;
  }
  .brand-name {
    position: absolute; left: 0; top: 122px; width: 100%;
    text-align: center; font-family: "Montserrat", sans-serif; font-weight: 400;
    font-size: 31px; letter-spacing: 12px; text-indent: 12px; color: var(--ink);
  }
  .tagline {
    position: absolute; left: 0; top: 168px; width: 100%;
    text-align: center; font-family: "Lato", sans-serif; font-weight: 900;
    font-size: 22px; letter-spacing: 1.5px; color: var(--ink);
  }
  .services { list-style: none; }
  .service {
    position: absolute; left: 18px; width: 442px; height: 50px;
    background: var(--c); color: var(--ribbon-text);
    font-family: "Lato", sans-serif; font-weight: 700; font-size: 22px;
    letter-spacing: 0.3px; line-height: 50px; text-align: center;
    box-shadow: 0 3px 5px rgba(0,0,0,0.25);
  }
  .service::before, .service::after {
    content: ""; position: absolute; top: 50px; width: 0; height: 0;
    border-top: 10px solid var(--d);
  }
  .service::before { left: 0; border-left: 26px solid transparent; }
  .service::after { right: 0; border-right: 26px solid transparent; }
  .service:nth-child(1) { top: 204px; --c: var(--navy); --d: var(--navy-fold); }
  .service:nth-child(2) { top: 268px; --c: var(--ocean); --d: var(--ocean-fold); }
  .service:nth-child(3) { top: 332px; --c: var(--teal); --d: var(--teal-fold); }
  .service:nth-child(4) { top: 396px; --c: var(--aqua); --d: var(--aqua-fold); }
  .service:nth-child(5) { top: 460px; --c: var(--sky); --d: var(--sky-fold); }
  .service:nth-child(6) { top: 524px; --c: var(--lagoon); --d: var(--lagoon-fold); }
  .service:nth-child(7) { top: 588px; --c: var(--teal); --d: var(--teal-fold); }
  .service:nth-child(8) { top: 652px; --c: var(--ocean); --d: var(--ocean-fold); }
  .service:nth-child(9) { top: 716px; --c: var(--navy); --d: var(--navy-fold); }

  .contact {
    position: absolute; left: 0; top: 778px; width: 100%; height: 50px;
    display: flex; align-items: center; justify-content: center; gap: 16px;
    font-family: "Lato", sans-serif; font-weight: 900; font-size: 42px; color: var(--ink);
  }
  .contact svg { width: 56px; height: 46px; }
</style>
</head>
<body>
<div class="canvas">
  <div class="magnet">
    <div class="linen-edge" role="img" aria-label="Grey linen texture border"></div>
    <div class="silver-panel"></div>

    <div class="brand-mark"></div>
    <div class="brand-name">NORTHLINE TAX</div>
    <div class="tagline">SPECIALISING IN:</div>

    <ul class="services">
      <li class="service">SMALL BUSINESS TAXATION</li>
      <li class="service">COMPANY &amp; TRUST RETURNS</li>
      <li class="service">FINANCIAL STATEMENTS</li>
      <li class="service">PARTNERSHIP TAXATION</li>
      <li class="service">BAS PREPARATION/LODGEMENT</li>
      <li class="service">CAPITAL GAINS TAX</li>
      <li class="service">BUSINESS START UPS</li>
      <li class="service">BUSINESS STRUCTURING</li>
      <li class="service">TAX PLANNING</li>
    </ul>

    <div class="contact">
      <svg viewBox="0 0 56 46" aria-hidden="true">
        <path d="M4 16 C4 4 52 4 52 16 L52 20 L40 20 L40 13 C34 11 22 11 16 13 L16 20 L4 20 Z" fill="#1f1f1f"/>
        <path d="M18 18 L38 18 L50 42 L6 42 Z" fill="#1f1f1f"/>
        <g fill="#d9d9d9">
          <circle cx="22" cy="27" r="2"/><circle cx="28" cy="27" r="2"/><circle cx="34" cy="27" r="2"/>
          <circle cx="21" cy="33" r="2"/><circle cx="28" cy="33" r="2"/><circle cx="35" cy="33" r="2"/>
          <circle cx="20" cy="39" r="2"/><circle cx="28" cy="39" r="2"/><circle cx="36" cy="39" r="2"/>
        </g>
      </svg>
      <span class="phone">0400 555 019</span>
    </div>
  </div>
</div>
</body>
</html>
```